PLUMBING POSTCARD DESIGN (MARKETING)

We are a local Plumbing business , Needing a post card to market domestic plumbing maintenance in my local area. The post card will have a magnet business card attached so allowance in design will need to be made. I have a slogan i want Incorporated into the design and is "TRY THE BEST, FLUSH THE REST"
I have attached my company name and logo to also incorporate into the design.
post card size 21cm L x 10cm H
business magnet card that will be attached to post card is 9cm L X 5.5cm H.
Post card will be one sided and will need following text inserted into design:
Pipevale would like to offer its fellow locals $40 off their next plumbing job. We pride ourselves in supplying the highest level of workmanship at the most competitive prices. CALL US TODAY
0431 582 907
Target Market(s)
Property owners (domestic market0
Industry/Entity Type
Plumbing
Requirements
Must have
- Eye catching, Slogan, company name and logo

```html
<!DOCTYPE html>
<html lang="en">
<head>
<meta charset="utf-8">
<title>Pipevale Postcard</title>
<link href="https://fonts.googleapis.com/css2?family=Montserrat:wght@400;500;600;700;800&family=Oswald:wght@500;600;700&display=swap" rel="stylesheet">
<style>
:root{
  --stage:#5e5e5e;
  --paper:#f6f6f7;
  --paper-2:#ececee;
  --blue:#1f93c4;
  --blue-dark:#1b7fb3;
  --blue-light:#22b0d8;
  --orange:#f26a36;
  --orange-mid:#f3913a;
  --yellow:#f7c544;
  --ink:#1c1c1c;
  --grey:#58585a;
  --white:#ffffff;
}
*{margin:0;padding:0;box-sizing:border-box}
html,body{width:1200px;height:720px;overflow:hidden}
body{background:var(--stage);position:relative;font-family:'Montserrat',sans-serif}
.postcard{position:absolute;left:30px;top:88px;width:1140px;height:543px;background:linear-gradient(135deg,var(--paper) 0%,var(--white) 45%,var(--paper-2) 100%);overflow:hidden}

.brand{position:absolute;left:66px;top:80px;display:flex;align-items:center;gap:14px}
.brand-dot{width:44px;height:44px;border-radius:50%;background:var(--blue)}
.brand-name{font-family:'Montserrat',sans-serif;font-weight:700;font-size:42px;color:var(--grey);letter-spacing:.5px}

.contact-pill{position:absolute;left:508px;top:44px;width:600px;height:37px;border-radius:19px;display:flex;overflow:hidden;color:var(--white);font-size:17px;font-weight:500}
.contact-pill .item{display:flex;align-items:center;gap:10px;padding-left:18px}
.contact-pill .mail{width:307px;background:linear-gradient(90deg,var(--blue-dark),var(--blue-light))}
.contact-pill .web{flex:1;background:linear-gradient(90deg,var(--orange),var(--yellow));padding-left:12px}
.contact-pill svg{width:20px;height:20px}

.slogan-band{position:absolute;left:0;top:144px;width:617px;height:146px;background:linear-gradient(90deg,var(--blue-dark),var(--blue-light))}
.slogan{position:absolute;left:57px;top:10px;color:var(--white);font-weight:800;font-size:57px;line-height:63px;letter-spacing:.5px}

.pitch{position:absolute;left:60px;top:302px;width:470px;font-size:16.6px;line-height:22.5px;color:var(--ink);font-weight:500}
.pitch .name{color:var(--blue);font-weight:700;text-transform:uppercase}
.pitch .tag{display:inline-block;background:linear-gradient(90deg,var(--orange),var(--yellow));color:var(--white);font-weight:700;padding:0 10px;margin:0 6px 0 2px;outline:1px dashed var(--blue);line-height:20px}
.pitch .accent{color:var(--orange);font-weight:700}

.call-band{position:absolute;left:0;top:0;width:1140px;height:543px}
.call-label{position:absolute;left:53px;top:408px;width:287px;height:43px;background:linear-gradient(90deg,var(--blue-dark),var(--blue-light));color:var(--white);font-weight:700;font-size:27px;display:flex;align-items:center;padding-left:19px;letter-spacing:.5px}
.call-number{position:absolute;left:53px;top:461px;display:flex;align-items:center;gap:12px}
.call-number .icon{width:54px;height:54px}
.call-number .digits{color:var(--white);font-weight:800;font-size:57px;letter-spacing:.5px}

.coupon{position:absolute;left:619px;top:108px;width:492px;height:300px;border:2px dashed var(--orange);border-radius:16px;overflow:hidden;background:var(--white)}
.coupon svg.bg{position:absolute;inset:0}
.offer{position:absolute;left:30px;top:14px;color:var(--white);font-family:'Oswald',sans-serif;font-weight:700}
.offer .amount{font-size:96px;line-height:96px}
.offer .off{font-size:36px;vertical-align:top;position:relative;top:6px;margin-left:6px}
.offer .detail{font-size:35px;line-height:37px;margin-top:8px;font-weight:600}
.coupon-phone{position:absolute;left:200px;top:222px;width:275px;display:flex;align-items:center;gap:8px;color:var(--white);font-family:'Oswald',sans-serif;font-weight:600;font-size:40px;line-height:48px;border-bottom:1.5px solid var(--white);padding-bottom:2px}
.coupon-phone .icon{width:36px;height:36px}
.coupon-address{position:absolute;left:200px;top:276px;width:275px;text-align:center;color:var(--white);font-family:'Oswald',sans-serif;font-weight:500;font-size:12.5px}

.emergency{position:absolute;width:470px;height:64px;font-family:'Oswald',sans-serif}
.emergency .hours{position:absolute;left:0;top:2px;width:176px;height:58px;border-radius:29px;background:linear-gradient(90deg,var(--blue-dark),var(--blue-light));border:3px solid var(--orange);color:var(--white);font-weight:700;font-style:italic;font-size:50px;line-height:50px;padding-left:22px}
.emergency .clock{position:absolute;left:144px;top:0;width:64px;height:64px}
.emergency .word{position:absolute;left:222px;top:-6px;color:var(--blue);font-weight:700;font-style:italic;font-size:30px;letter-spacing:11.5px}
.emergency .service{position:absolute;left:210px;top:32px;width:256px;height:30px;background:linear-gradient(90deg,var(--orange),var(--yellow));transform:skewX(-12deg)}
.emergency .service span{display:block;transform:skewX(12deg);color:var(--white);font-weight:700;font-style:italic;font-size:26px;line-height:30px;padding-left:12px;letter-spacing:.3px}
.emergency.large{left:630px;top:448px}
.emergency.small{left:224px;top:172px;transform:scale(.53);transform-origin:left top}
</style>
</head>
<body>
<div class="postcard">

  <div class="brand">
    <span class="brand-dot"></span>
    <span class="brand-name">PIPEVALE</span>
  </div>

  <div class="contact-pill">
    <div class="item mail">
      <svg viewBox="0 0 24 24" fill="none" stroke="#fff" stroke-width="1.6"><rect x="2" y="5" width="20" height="14" rx="1"/><path d="M2 5l10 8 10-8M2 19l7-7M22 19l-7-7"/></svg>
      sam@pipevale.com.au
    </div>
    <div class="item web">
      <svg viewBox="0 0 24 24" fill="none" stroke="#fff" stroke-width="1.6"><circle cx="12" cy="12" r="9"/><ellipse cx="12" cy="12" rx="4" ry="9"/><path d="M3 12h18M5 7h14M5 17h14"/></svg>
      www.pipevale.com.au
    </div>
  </div>

  <div class="slogan-band">
    <h1 class="slogan">TRY THE BEST,<br>FLUSH THE REST</h1>
  </div>

  <p class="pitch"><span class="name">Pipevale</span> would like to offer its fellow locals <span class="tag">$40 OFF</span> their next plumbing job. We pride ourselves in supplying the highest level of workmanship at the <span class="accent">most competitive prices.</span></p>

  <svg class="call-band" viewBox="0 0 1140 543" aria-hidden="true">
    <defs>
      <linearGradient id="warm" x1="0" x2="1" y1="0" y2="0">
        <stop offset="0" stop-color="#f26a36"/><stop offset=".6" stop-color="#f3913a"/><stop offset="1" stop-color="#f7c544"/>
      </linearGradient>
    </defs>
    <path d="M0 432 H545 Q556 432 562 440 L618 520 Q628 533 645 533 H1140 V543 H0 Z" fill="url(#warm)"/>
  </svg>

  <div class="call-label">CALL US TODAY</div>
  <div class="call-number">
    <svg class="icon" viewBox="0 0 54 54"><circle cx="27" cy="27" r="26" fill="#fff"/><circle cx="27" cy="27" r="22" fill="#1f93c4"/><g transform="translate(15 15)"><path d="M6.6 10.8c1.4 2.8 3.8 5.1 6.6 6.6l2.2-2.2c.3-.3.7-.4 1-.2 1.1.4 2.3.6 3.6.6.6 0 1 .4 1 1V20c0 .6-.4 1-1 1C10.6 21 3 13.4 3 4c0-.6.4-1 1-1h3.5c.6 0 1 .4 1 1 0 1.2.2 2.4.6 3.6.1.3 0 .7-.2 1z" fill="#fff"/></g></svg>
    <span class="digits">0431 582 907</span>
  </div>

  <div class="coupon">
    <svg class="bg" viewBox="0 0 492 300" preserveAspectRatio="none">
      <defs>
        <linearGradient id="cblue" x1="0" x2="1" y1="1" y2="0">
          <stop offset="0" stop-color="#1b7fb3"/><stop offset="1" stop-color="#22b0d8"/>
        </linearGradient>
        <linearGradient id="cwarm" x1="0" x2="1">
          <stop offset="0" stop-color="#f26a36"/><stop offset="1" stop-color="#f7c544"/>
        </linearGradient>
        <linearGradient id="photo" x1="0" x2="1" y1="0" y2="1">
          <stop offset="0" stop-color="#d9dde2"/><stop offset=".5" stop-color="#b9c2cc"/><stop offset="1" stop-color="#8d98a5"/>
        </linearGradient>
      </defs>
      <polygon points="264,0 492,0 492,158 205,158" fill="url(#photo)" role="img" aria-label="Photo of a smiling plumber in blue overalls holding a wrench and toolbox beside a white company van"/>
      <polygon points="194,215 492,215 492,300 160,300" fill="url(#cwarm)"/>
      <polygon points="0,0 276,0 161,300 0,300" fill="url(#cblue)"/>
    </svg>
    <div class="offer">
      <div><span class="amount">$40</span><span class="off">OFF</span></div>
      <div class="detail">ON YOUR<br>NEXT<br>PLUMBING<br>JOB</div>
    </div>
    <div class="emergency small">
      <div class="hours">24/7</div>
      <svg class="clock" viewBox="0 0 64 64"><defs><linearGradient id="clk1" x1="0" x2="1"><stop offset="0" stop-color="#f26a36"/><stop offset="1" stop-color="#f7c544"/></linearGradient></defs><circle cx="32" cy="32" r="30" fill="url(#clk1)" stroke="#fff" stroke-width="3"/><circle cx="32" cy="32" r="20" fill="none" stroke="#fff" stroke-width="2" stroke-dasharray="2 4"/><path d="M32 20v12l8 -6" fill="none" stroke="#fff" stroke-width="2.5" stroke-linecap="round"/><g transform="translate(14 30) scale(1.1)"><path d="M6.6 10.8c1.4 2.8 3.8 5.1 6.6 6.6l2.2-2.2c.3-.3.7-.4 1-.2 1.1.4 2.3.6 3.6.6.6 0 1 .4 1 1V20c0 .6-.4 1-1 1C10.6 21 3 13.4 3 4c0-.6.4-1 1-1h3.5c.6 0 1 .4 1 1 0 1.2.2 2.4.6 3.6.1.3 0 .7-.2 1z" fill="#fff"/></g></svg>
      <div class="word">EMERGENCY</div>
      <div class="service"><span>PLUMBING SERVICE</span></div>
    </div>
    <div class="coupon-phone">
      <svg class="icon" viewBox="0 0 54 54"><circle cx="27" cy="27" r="26" fill="#fff"/><circle cx="27" cy="27" r="22" fill="#1f93c4"/><g transform="translate(15 15)"><path d="M6.6 10.8c1.4 2.8 3.8 5.1 6.6 6.6l2.2-2.2c.3-.3.7-.4 1-.2 1.1.4 2.3.6 3.6.6.6 0 1 .4 1 1V20c0 .6-.4 1-1 1C10.6 21 3 13.4 3 4c0-.6.4-1 1-1h3.5c.6 0 1 .4 1 1 0 1.2.2 2.4.6 3.6.1.3 0 .7-.2 1z" fill="#fff"/></g></svg>
      0431 582 907
    </div>
    <div class="coupon-address">14 Harbour St Westbrook 4350, Queensland</div>
  </div>

  <div class="emergency large">
    <div class="hours">24/7</div>
    <svg class="clock" viewBox="0 0 64 64"><defs><linearGradient id="clk2" x1="0" x2="1"><stop offset="0" stop-color="#f26a36"/><stop offset="1" stop-color="#f7c544"/></linearGradient></defs><circle cx="32" cy="32" r="30" fill="url(#clk2)" stroke="#fff" stroke-width="3"/><circle cx="32" cy="32" r="20" fill="none" stroke="#fff" stroke-width="2" stroke-dasharray="2 4"/><path d="M32 20v12l8 -6" fill="none" stroke="#fff" stroke-width="2.5" stroke-linecap="round"/><g transform="translate(14 30) scale(1.1)"><path d="M6.6 10.8c1.4 2.8 3.8 5.1 6.6 6.6l2.2-2.2c.3-.3.7-.4 1-.2 1.1.4 2.3.6 3.6.6.6 0 1 .4 1 1V20c0 .6-.4 1-1 1C10.6 21 3 13.4 3 4c0-.6.4-1 1-1h3.5c.6 0 1 .4 1 1 0 1.2.2 2.4.6 3.6.1.3 0 .7-.2 1z" fill="#fff"/></g></svg>
    <div class="word">EMERGENCY</div>
    <div class="service"><span>PLUMBING SERVICE</span></div>
  </div>

</div>
</body>
</html>
```